Vessary Wine Label

We are seeking a wine label. Clean, minimalist, pen & ink art. We already make meads and ciders, (labels online have not all been updated- bottom few have) which have a craft feel, but now would like a simple wine label for our new line of wines. We have all the necessary verbage already required for wine labels. We just need room on the sides (will use one large label) to print the description of our business, govt. warnings, etc. We would like to use our last name - Vessary- with some simple pen and ink art in the upper right hand corner of a bumble bee with some botanical somethings. We make all of our products on a working farm with bees, and our farm logo is a bumble bee...so it's just a little tie in there. We will keep all the labels the same apart from the varietal, vintage, and appellation (in some cases). Label inspiration is something like Tolvic. Preferably printing on cream colored label paper. First wine to be bottled is a black Spanish Rose. Thank you for your consideration and your time.

Target Market(s)

35 -60 demo. red wine drinkers

Industry/Entity Type

French Winery

Colors

Designer to choose colors to be used in the design.

Requirements
Nice to have
• pen and ink art

```html
<!DOCTYPE html>
<html lang="en">
<head>
<meta charset="UTF-8">
<title>Vessary Rosé – Wine Label</title>
<link rel="stylesheet" href="https://fonts.googleapis.com/css2?family=Playfair+Display:wght@400;500&display=swap">
<style>
  :root {
    --backdrop: #ececec;
    --label-black: #000000;
    --gold: #efe19a;
    --rose-pink: #d8348a;
    --glass-deep: #8a1553;
    --glass-bright: #c4377f;
    --fine-print: #b9b9b9;
  }
  html, body {
    margin: 0;
    padding: 0;
    width: 1200px;
    height: 1199px;
    overflow: hidden;
    background: var(--backdrop);
  }
  .canvas {
    position: relative;
    width: 1200px;
    height: 1199px;
  }
  .wine-label {
    position: absolute;
    left: 382px;
    top: 100px;
    width: 436px;
    height: 1000px;
    background: var(--label-black);
    font-family: "Playfair Display", Georgia, serif;
  }
  .label-brand {
    position: absolute;
    left: 60px;
    top: 300px;
    margin: 0;
    font-weight: 400;
    font-size: 84px;
    line-height: 1;
    color: var(--gold);
    letter-spacing: 0.5px;
  }
  .label-varietal {
    position: absolute;
    left: 270px;
    top: 405px;
    margin: 0;
    font-weight: 400;
    font-size: 34px;
    line-height: 1;
    color: var(--rose-pink);
  }
  .glass-artwork {
    position: absolute;
    left: 166px;
    top: 680px;
    width: 96px;
    height: 225px;
  }
  .label-fineprint {
    position: absolute;
    bottom: 22px;
    margin: 0;
    font-size: 14px;
    letter-spacing: 1px;
    color: var(--fine-print);
  }
  .volume { left: 22px; }
  .alcohol { right: 22px; font-size: 12px; }
</style>
</head>
<body>
<main class="canvas">
  <section class="wine-label">
    <h1 class="label-brand">Vessary</h1>
    <p class="label-varietal">Rosé</p>
    <svg class="glass-artwork" viewBox="0 0 96 225" role="img" aria-label="Wine glass illustration formed from pink grape dots">
      <defs>
        <linearGradient id="glassTone" x1="0" y1="0" x2="0" y2="1">
          <stop offset="0" stop-color="var(--glass-bright)"/>
          <stop offset="1" stop-color="var(--glass-deep)"/>
        </linearGradient>
      </defs>
      <rect x="0" y="0" width="96" height="225" fill="url(#glassTone)"/>
    </svg>
    <p class="label-fineprint volume">750 ML.</p>
    <p class="label-fineprint alcohol">ALC 11.5% BY VOL.</p>
  </section>
</main>
</body>
</html>
```